Ridge Lass Collective (Flyer)

I want a flyer to advertise my service.
Details below, and logo's to use are attached.

A girls only after school program, 11-14yrs, as OSHC is no longer avail, dedicated to coaching & mentoring our girls into strong, independent young women.

The Brainchild of Rebecca Tolland, Ridge Lass Collective was created to address the growing demand for after school/school holiday supervision for kids moving from primary into high school, when OSHC ceases to exist.
With over 12 years experience mentoring and coaching young women in the corporate world, Bec decided to leave her role as a Director with Pemberly Savings, and follow her passion.
Bec, along with her sister Juliette, who has over 10 years experience in local communities as a Youth Worker, and is also a qualified Enrolled Nurse, embarked on building a program designed to keep parents happy (by knowing their girls are safe) and dedicated to coaching and mentoring our girls into strong, independent young women.
Open every afternoon and during school holidays, we look to offer;
- Daily meditation
- Healthy snacks
- Dedicated homework time
- Organised group activity, led by qualified instructors (yoga, fitness class, soccer etc)
- Regular guests speakers, addressing issues/concerns for young people today
- SOCIAL MEDIA FREE ZONE

Located 318 Garvey St, Baulkham Hills (across from Oakmere Medical Centre)
Open 3-6pm Monday to Friday

Facebook page: http://fb.me/ridgelasscollective
Email: info@ridgelasscollective.com.au
Mobile: 0487615093

Target Market(s)

Parents of teenage girls, teenage girls 11-14 years

Industry/Entity Type

School

Font styles to use
Sans Serif

Colors
b768aa
e667a6

Requirements
Must have
• What progam is - see brief
• Who runs it
Should not have
• Not be too busy, not overly mature images

```html
<!DOCTYPE html>
<html lang="en">
<head>
<meta charset="utf-8">
<title>Ridge Lass Collective – Flyer</title>
<link rel="stylesheet" href="https://fonts.googleapis.com/css2?family=Dancing+Script:wght@700&family=Lato:wght@400;700;900&display=swap">
<style>
  :root {
    --magenta: #e8399a;
    --pink: #e667a6;
    --navy: #1d1a4e;
    --ink: #2b2b3a;
    --lavender: #d8d5f6;
    --lilac: #b768aa;
    --paper: #ffffff;
    --backdrop: #eef0f3;
  }
  * { box-sizing: border-box; margin: 0; padding: 0; }
  html, body { width: 1200px; height: 912px; overflow: hidden; }
  body {
    background: var(--backdrop);
    font-family: "Lato", sans-serif;
    color: var(--ink);
    position: relative;
  }
  .flyer {
    position: absolute;
    left: 290px; top: 17px;
    width: 620px; height: 878px;
    background: var(--paper);
    overflow: hidden;
    box-shadow: 0 2px 10px rgba(0,0,0,.12);
  }
  .brand {
    position: absolute; left: 40px; top: 96px;
    display: flex; align-items: center; gap: 12px;
  }
  .brand-dot {
    width: 46px; height: 46px; border-radius: 50%;
    background: var(--lavender);
  }
  .brand-name {
    font-family: "Lato", sans-serif; font-weight: 900;
    font-size: 26px; line-height: 1.05; color: var(--magenta);
    width: 150px;
  }
  .hero-ring {
    position: absolute; left: 236px; top: -60px;
    width: 410px; height: 410px; border-radius: 50%;
    border: 3px solid var(--navy);
    padding: 6px;
  }
  .hero-photo {
    width: 100%; height: 100%; border-radius: 50%;
    border: 9px solid var(--magenta);
    background: linear-gradient(160deg, #f4e1c8 0%, #c9a98a 35%, #6f6a78 65%, #d9d3cc 100%);
  }
  .inset-ring {
    position: absolute; left: 218px; top: 216px;
    width: 168px; height: 168px; border-radius: 50%;
    border: 3px solid var(--navy); padding: 5px; background: var(--paper);
  }
  .inset-photo {
    width: 100%; height: 100%; border-radius: 50%;
    border: 7px solid var(--magenta);
    background: linear-gradient(180deg, #e9ecef 0%, #cfd3da 100%);
  }
  .hours { position: absolute; left: 40px; top: 362px; }
  .hours-open {
    font-family: "Dancing Script", cursive; font-weight: 700;
    font-size: 84px; line-height: .9; color: var(--magenta);
  }
  .hours-time {
    font-family: "Dancing Script", cursive; font-weight: 700;
    font-size: 72px; line-height: .95; color: var(--navy); margin-left: 30px;
  }
  .hours-days {
    font-weight: 900; font-size: 31px; line-height: 1.2; color: var(--magenta);
    margin-left: 6px; margin-top: 2px;
  }
  .content { position: absolute; left: 40px; top: 566px; width: 540px; }
  .lead {
    font-weight: 900; font-size: 15px; line-height: 1.25; color: var(--navy);
    margin-bottom: 7px;
  }
  .body-copy { font-size: 9.6px; line-height: 1.35; margin-bottom: 5px; }
  .offer-title {
    color: var(--magenta); font-weight: 700; font-size: 11px; margin: 7px 0 4px;
  }
  .offer-columns {
    display: grid; grid-template-columns: 1fr 1.25fr; column-gap: 20px;
  }
  .offer-list { list-style: none; font-size: 10.2px; line-height: 1.35; }
  .offer-list li { position: relative; padding-left: 12px; }
  .offer-list li::before {
    content: ""; position: absolute; left: 0; top: 4px;
    width: 6px; height: 6px; border-radius: 50%; background: var(--magenta);
  }
  .footer {
    position: absolute; left: 0; bottom: 0; width: 100%; height: 64px;
    background: var(--lavender); border-top: 5px solid var(--magenta);
    display: flex; align-items: center; padding: 0 32px;
    font-size: 10.5px; color: var(--navy);
  }
  .footer-col { display: flex; flex-direction: column; gap: 6px; white-space: nowrap; }
  .footer-col.right { margin-left: auto; padding-left: 18px; border-left: 1px solid var(--navy); }
  .contact { display: flex; align-items: center; gap: 7px; }
  .contact svg { flex: none; }
  .square-mark { width: 12px; height: 12px; background: var(--magenta); border-radius: 2px; flex: none; }
</style>
</head>
<body>
  <main class="flyer">
    <div class="hero-ring">
      <div class="hero-photo" role="img" aria-label="Photo of a cheerful girl in a striped top jumping on a sunny beach"></div>
    </div>
    <div class="inset-ring">
      <div class="inset-photo" role="img" aria-label="Photo of a white t-shirt printed with the program name"></div>
    </div>

    <div class="brand">
      <span class="brand-dot"></span>
      <span class="brand-name">Ridge Lass Collective</span>
    </div>

    <section class="hours">
      <div class="hours-open">Open</div>
      <div class="hours-time">3-6pm</div>
      <div class="hours-days">Monday to Friday</div>
    </section>

    <section class="content">
      <p class="lead">A girls only after school program, 11-14yrs, as OSHC is no longer avail, dedicated to coaching &amp; mentoring our girls into strong, independent young women.</p>
      <p class="body-copy">The Brainchild of Rebecca Tolland, Ridge Lass Collective was created to address the growing demand for after school/school holiday supervision for kids moving from primary into high school, when OSHC ceases to exist.</p>
      <p class="body-copy">With over 12 years experience mentoring and coaching young women in the corporate world, Bec decided to leave her role as a Director with Pemberly Savings, and follow her passion. Bec, along with her sister Juliette, who has over 10 years experience in local communities as a Youth Worker, and is also a qualified Enrolled Nurse, embarked on building a program designed to keep parents happy (by knowing their girls are safe) and dedicated to coaching and mentoring our girls into strong, independent young women.</p>
      <p class="offer-title">Open every afternoon and during school holidays, we look to offer:</p>
      <div class="offer-columns">
        <ul class="offer-list">
          <li>Daily meditation</li>
          <li>Healthy snacks</li>
          <li>Dedicated homework time</li>
          <li>Social Media FREE ZONE</li>
        </ul>
        <ul class="offer-list">
          <li>Organised group activity, led by qualified instructors (yoga, fitness class, soccer etc)</li>
          <li>Regular guests speakers, addressing issues/concerns for young people today</li>
        </ul>
      </div>
    </section>

    <footer class="footer">
      <div class="footer-col">
        <span class="contact">
          <svg width="13" height="12" viewBox="0 0 13 12" aria-hidden="true"><path d="M6.5 0 13 5.5h-2V12H8V8H5v4H2V5.5H0z" fill="var(--magenta)"/></svg>
          318 Garvey St, Baulkham Hills (across from Oakmere Medical Centre)
        </span>
        <span class="contact">
          <svg width="13" height="10" viewBox="0 0 13 10" aria-hidden="true"><rect width="13" height="10" rx="1" fill="var(--magenta)"/><path d="M0.5 1 6.5 6 12.5 1" stroke="#fff" stroke-width="1.2" fill="none"/></svg>
          info@ridgelasscollective.com.au
        </span>
      </div>
      <div class="footer-col right">
        <span class="contact"><span class="square-mark"></span>http://fb.me/ridgelasscollective</span>
        <span class="contact">
          <svg width="12" height="12" viewBox="0 0 12 12" aria-hidden="true"><rect width="12" height="12" rx="2" fill="var(--magenta)"/><path d="M3.2 2.5c.4-.3.9-.2 1.1.2l.6 1.2c.2.4 0 .8-.3 1l-.4.3c.4.9 1 1.6 1.9 2l.3-.4c.3-.3.7-.4 1-.2l1.2.6c.4.2.5.7.2 1.1l-.4.5c-.5.5-1.3.6-2 .3C4.6 8.3 3.2 6.9 2.4 5c-.3-.7-.1-1.5.4-2z" fill="#fff"/></svg>
          CALL US: 0487615093
        </span>
      </div>
    </footer>
  </main>
</body>
</html>
```